Modern Employee Handbook Cover Design Needed

I need help. I am designing a 50+ page Employee Handbook and want a great cover design. I'm looking for a great cover because our company has changed so much in the past years since the last handbook was published and I want to signify and celebrate all the positive things we have done. It may not seem like such a big deal but I'm trying to make a big impact.

I'm looking for something interesting. Employee Handbooks are the most boring things int he world but I don't ours to LOOK that way. I want creative, modern, slick, clean, whatever you want that would make someone want to look at (even if it is for a second). It does NOT need to even be called an Employee Handbook (I'm really open to ideas)

This will be a typical 8.5 x 11 book format. 70% of our employees are under the age of 40 and are in CA, MA, FL, and IN.

The final design should communicate that we are not the same company we were a few years ago but instead we are more modern and current.

Target Market(s)

Most of our employees are under 40 years old. They are well educated. We are a national company with employees in CA, MA, FL and IN

Industry/Entity Type

Education

Font styles to use
Serif
Sans Serif
Other font styles liked:
• I like the fonts used by velmo but am open to ANY fonts.

Requirements
Must have
• Modern, up to date designs, unexpected, unique, cool, etc...
Should not have
• I don't like the typical teamwork images, world and globe things, or tree supporting branch type things that Human Resources and Employee Handbooks often is represented by in print. They are so boring to me. https://www.trelvasearch.com/search?q=human+resources+handbook&source=lnms&tbm=isch&sa=X&ved=0ahUKEwjl1oWHt67RAhULw1QKHWTaB0oQ_AUICCgB&biw=1920&bih=950
• No stick figures standing in a row or shaking hands. Stuff like that is so old.
• Our clients are young adults with Autism but I don't want puzzle pieces which is a universal symbol of Autism.

```html
<!DOCTYPE html>
<html lang="en">
<head>
<meta charset="utf-8">
<title>Employee Handbook Cover</title>
<link href="https://fonts.googleapis.com/css2?family=Raleway:wght@400;500;700&display=swap" rel="stylesheet">
<style>
  :root {
    --page-bg: #e9ebee;
    --sky: #7fa3d6;
    --mist: #b9c8d6;
    --peach: #d9b9a6;
    --teal: #8fb1bf;
    --navy: #1f4f97;
    --accent: #2aa3d3;
    --white: #ffffff;
    --logo-ink: #1f3f8a;
  }
  * { margin: 0; padding: 0; box-sizing: border-box; }
  html, body {
    width: 1200px;
    height: 850px;
    overflow: hidden;
    background: var(--page-bg);
    font-family: "Raleway", sans-serif;
  }
  .canvas {
    width: 1200px;
    height: 850px;
    display: flex;
    align-items: center;
    justify-content: center;
  }
  .cover {
    position: relative;
    width: 618px;
    height: 800px;
    overflow: hidden;
    box-shadow: 0 6px 24px rgba(30, 40, 60, 0.18);
  }
  .cover-art {
    position: absolute;
    inset: 0;
    background:
      radial-gradient(ellipse at 85% 15%, var(--peach) 0%, rgba(217,185,166,0) 60%),
      radial-gradient(ellipse at 40% 75%, var(--teal) 0%, rgba(143,177,191,0) 55%),
      linear-gradient(120deg, var(--sky) 0%, var(--mist) 45%, var(--peach) 100%);
  }
  .title {
    position: absolute;
    left: 58px;
    top: 430px;
    color: var(--white);
    font-size: 76px;
    line-height: 1;
    letter-spacing: 1px;
  }
  .title-strong { display: block; font-weight: 700; }
  .title-light { display: block; font-weight: 500; }
  .brand-band {
    position: absolute;
    left: 0;
    top: 620px;
    width: 618px;
    height: 102px;
  }
  .brand-band svg { position: absolute; inset: 0; }
  .brand-name {
    position: absolute;
    left: 34px;
    top: 36px;
    color: var(--logo-ink);
    font-weight: 700;
    font-size: 24px;
  }
  .program-name {
    position: absolute;
    left: 250px;
    top: 37px;
    color: var(--white);
    font-weight: 500;
    font-size: 24px;
    letter-spacing: 0.3px;
  }
</style>
</head>
<body>
  <main class="canvas">
    <section class="cover">
      <div class="cover-art" role="img" aria-label="Soft low-poly geometric gradient in blue and peach tones"></div>
      <h1 class="title">
        <span class="title-strong">EMPLOYEE</span>
        <span class="title-light">HANDBOOK</span>
      </h1>
      <div class="brand-band">
        <svg width="618" height="102" viewBox="0 0 618 102" aria-hidden="true">
          <polygon points="0,0 204,0 176,102 0,102" fill="var(--white)"/>
          <polygon points="204,0 226,0 198,102 176,102" fill="var(--accent)"/>
          <polygon points="226,0 618,0 618,102 198,102" fill="var(--navy)"/>
        </svg>
        <span class="brand-name">Bridgeway</span>
        <span class="program-name">Bridgeway Learning Program</span>
      </div>
    </section>
  </main>
</body>
</html>
```